Letterhead design for Sleep Consulting Business

I'm looking for a new letterhead (heading/footer) design for my Sleep Consulting Business, I work with families to help their children improve their sleep.

The heading/footer will used in Microsoft Word Only-to be used for all of my documents such as writing Sleep Plans. I need to utilize as much working space in the document as possible. This will NOT be printed out on paper- it will only be used for heading/footer on microsoft word, then emailed to clients, who may print it at home.

My brand colors:
Dark Blue Hex: 1F2A42
Lighter Blueish Hex: 90BEC9
You're welcome to check out my website for inspiration- it is freshly created with other colors as well, and I love the outcome. www.hollowpinerest.com

Target Market(s)

Tired parents

Font styles to use
Script
Other font styles liked:
• Great Vibe, Lato or Just Another Hand are all used currently for my brand. Open to other options.

Requirements
Must have
• The letterhead (heading/footer) MUST be kept narrow (height-wise), so I have plenty of space on my document, while including important information.

It should look professional on screen, and when printed.

Must include my business name OR logo (Hollow Pine Sleep Consulting), and my email address. Mara@hollowpinerest.com

Website is optional, not required, just if you need to fill in a spot: www.hollowpinerest.com

```html
<!DOCTYPE html>
<html lang="en">
<head>
<meta charset="utf-8">
<title>Hollow Pine Sleep Consulting — Letterhead</title>
<link rel="stylesheet" href="https://fonts.googleapis.com/css2?family=Montserrat:wght@400;500;600&display=swap">
<style>
  :root {
    --navy: #0f1c45;
    --mint: #92e0d5;
    --paper: #fdfdfd;
    --white: #ffffff;
  }
  * { margin: 0; padding: 0; box-sizing: border-box; }
  html, body { width: 849px; height: 1200px; overflow: hidden; background: var(--paper); }
  .letterhead {
    position: relative;
    width: 849px;
    height: 1200px;
    background: var(--paper);
    font-family: "Montserrat", Arial, sans-serif;
    overflow: hidden;
  }
  .header-shapes, .footer-wave { position: absolute; left: 0; display: block; }
  .header-shapes { top: 0; width: 849px; height: 92px; }
  .footer-wave { top: 1100px; width: 849px; height: 100px; }

  .brand {
    position: absolute;
    left: 68px;
    top: 9px;
    height: 62px;
    display: flex;
    align-items: center;
    gap: 12px;
  }
  .brand-dot {
    width: 60px;
    height: 60px;
    border-radius: 50%;
    background: var(--mint);
    flex: none;
  }
  .brand-name {
    color: var(--navy);
    font-weight: 600;
    font-size: 16px;
    letter-spacing: 0.3px;
    white-space: nowrap;
  }

  .contact {
    position: absolute;
    left: 530px;
    top: 12px;
    list-style: none;
    color: var(--white);
    font-size: 13.5px;
    font-weight: 500;
    letter-spacing: 0.2px;
  }
  .contact li {
    display: flex;
    align-items: center;
    gap: 9px;
    height: 20px;
    margin-bottom: 9px;
  }
  .contact-icon { width: 18px; height: 18px; flex: none; }
</style>
</head>
<body>
<div class="letterhead">
  <svg class="header-shapes" viewBox="0 0 849 92" aria-hidden="true">
    <polygon points="0,78 431,78 473,0 484,0 436,82 0,82" fill="var(--mint)"/>
    <polygon points="485,0 849,0 849,82 444,82" fill="var(--navy)"/>
    <rect x="0" y="87" width="849" height="3" fill="var(--navy)"/>
  </svg>

  <div class="brand">
    <span class="brand-dot"></span>
    <span class="brand-name">Hollow Pine Sleep Consulting</span>
  </div>

  <ul class="contact">
    <li>
      <svg class="contact-icon" viewBox="0 0 18 18" aria-hidden="true">
        <rect x="1" y="4" width="16" height="11" fill="none" stroke="var(--white)" stroke-width="1.4"/>
        <polyline points="1,4 9,10.5 17,4" fill="none" stroke="var(--white)" stroke-width="1.4"/>
        <line x1="1" y1="15" x2="7" y2="9" stroke="var(--white)" stroke-width="1.2"/>
        <line x1="17" y1="15" x2="11" y2="9" stroke="var(--white)" stroke-width="1.2"/>
      </svg>
      <span>Mara@hollowpinerest.com</span>
    </li>
    <li>
      <svg class="contact-icon" viewBox="0 0 18 18" aria-hidden="true">
        <circle cx="9" cy="9" r="7.8" fill="none" stroke="var(--white)" stroke-width="1.1"/>
        <ellipse cx="9" cy="9" rx="3.6" ry="7.8" fill="none" stroke="var(--white)" stroke-width="0.9"/>
        <line x1="1.2" y1="9" x2="16.8" y2="9" stroke="var(--white)" stroke-width="0.9"/>
        <line x1="2.5" y1="5" x2="15.5" y2="5" stroke="var(--white)" stroke-width="0.8"/>
        <line x1="2.5" y1="13" x2="15.5" y2="13" stroke="var(--white)" stroke-width="0.8"/>
      </svg>
      <span>www.hollowpinerest.com</span>
    </li>
  </ul>

  <svg class="footer-wave" viewBox="0 0 849 100" preserveAspectRatio="none" aria-hidden="true">
    <path d="M0 71 C 90 36, 200 24, 380 46 S 690 104, 849 56 L849 100 L0 100 Z" fill="var(--mint)"/>
    <path d="M0 77 C 100 48, 220 42, 380 60 S 700 112, 849 59 L849 100 L0 100 Z" fill="var(--navy)"/>
  </svg>
</div>
</body>
</html>
```